Brochure for financial planning firm

I need a brochure designed that will be folded into three panels idealy. I will provide the copy, logo, and some of the pictures.

Our primary business is finding investors for large-scale real estate developments.

Some of the pictures will have to come from outside this website given the file sizes. Please click the following link to download pictures of projects we have raised money for:

https://files.tarnuvex.net/share/7QmW2rLp94ZxKdTbYhVcNs3EaUfJ8gGo?view=open

Target Market(s)

People Ages 30 to 75. That are unsatisfied with their retirement investments

Industry/Entity Type

Financial

Requirements
Must have
• Addition to copy:
• To recieve information on our latest investments visit www.cloverpathsavings.ca
• Contact info:
• Tarrowby Wealth Management Inc.
• 4 Pellam Rd. W.
• Suite K300
• Hamilton, ON K2R 7T5
• Office: (905) 463-2918
• www.tarrowbywm.com
• The brochure must have somewhere printed on it near our contact info: RBQT Lic # 40963

```html
<!DOCTYPE html>
<html lang="en">
<head>
<meta charset="utf-8">
<title>Tarrowby Wealth Management – Tri-fold Brochure</title>
<link rel="stylesheet" href="https://fonts.googleapis.com/css2?family=Tinos:wght@400;700&display=swap">
<style>
  :root {
    --page-bg: #ececec;
    --ink-dark: #2e2b31;
    --ink-dark-2: #3a363d;
    --teal: #2f9e88;
    --teal-soft: #4fbba4;
    --teal-glass: rgba(79, 187, 164, 0.62);
    --white: #ffffff;
    --text-dark: #1f1d22;
  }
  * { box-sizing: border-box; margin: 0; padding: 0; }
  html, body { width: 1200px; height: 1000px; overflow: hidden; }
  body {
    background: var(--page-bg);
    font-family: "Tinos", "Times New Roman", serif;
    position: relative;
  }
  .brochure {
    position: absolute;
    left: 50px; top: 140px;
    width: 1100px; height: 720px;
    box-shadow: 0 18px 40px rgba(0,0,0,0.18);
    overflow: hidden;
  }
  .brochure-art { position: absolute; inset: 0; width: 1100px; height: 720px; display: block; }

  .intro-copy {
    position: absolute; left: 36px; top: 395px; width: 300px;
    color: var(--text-dark); font-size: 17px; line-height: 1.22;
  }
  .intro-copy .highlight { display: block; margin-top: 10px; font-weight: 700; letter-spacing: .5px; }

  .headline {
    position: absolute; left: 400px; top: 48px; width: 300px;
    text-align: right; color: var(--white);
    font-size: 22px; font-weight: 400; line-height: 1.55;
  }

  .contact {
    position: absolute; left: 400px; top: 470px; width: 300px;
    text-align: right; color: var(--white); font-size: 16px; line-height: 1.3;
    font-style: normal;
  }
  .contact-title { font-size: 24px; font-weight: 700; margin-bottom: 12px; }
  .contact-gap { margin-top: 14px; }
  .licence { margin-top: 10px; font-size: 14px; }
  .latest-investments { margin-top: 6px; font-size: 13px; line-height: 1.25; }

  .brand {
    position: absolute; left: 790px; top: 300px;
    display: flex; align-items: center; gap: 10px;
  }
  .brand-mark { width: 30px; height: 30px; background: var(--teal-soft); }
  .brand-name { color: var(--white); font-size: 24px; letter-spacing: 2px; }

  .cover-copy {
    position: absolute; left: 760px; top: 560px; width: 320px;
    color: var(--white); font-size: 19px; line-height: 1.25;
  }
  .cover-copy strong { font-weight: 700; }
  .cover-copy .cta { display: block; margin-top: 10px; font-size: 16px; font-weight: 700; color: var(--text-dark); }
</style>
</head>
<body>
<main class="brochure">
  <svg class="brochure-art" viewBox="0 0 1100 720" xmlns="http://www.w3.org/2000/svg">
    <defs>
      <linearGradient id="towerPhoto" x1="0" y1="0" x2="0" y2="1">
        <stop offset="0" stop-color="#5f7fbf"/>
        <stop offset=".35" stop-color="#a7b5d4"/>
        <stop offset=".6" stop-color="#6c6f7a"/>
        <stop offset=".85" stop-color="#7b6a55"/>
        <stop offset="1" stop-color="#4a5a3e"/>
      </linearGradient>
      <linearGradient id="townhousePhoto" x1="0" y1="0" x2="0" y2="1">
        <stop offset="0" stop-color="#5c8fcf"/>
        <stop offset=".45" stop-color="#e8e8e6"/>
        <stop offset=".75" stop-color="#a9673f"/>
        <stop offset="1" stop-color="#5f7552"/>
      </linearGradient>
    </defs>

    <!-- Left panel -->
    <g role="img" aria-label="Photo of a modern residential tower at dusk">
      <rect x="0" y="0" width="367" height="720" fill="url(#towerPhoto)"/>
    </g>
    <path d="M0 0 L367 0 L367 60 C250 120 120 150 0 140 Z" fill="var(--teal-glass)"/>
    <path d="M0 180 C120 260 260 300 367 310 L367 720 L0 720 Z" fill="var(--teal-glass)"/>
    <path d="M0 620 C140 560 260 520 367 505 L367 720 L0 720 Z" fill="var(--teal-glass)"/>

    <!-- Middle panel -->
    <rect x="367" y="0" width="366" height="720" fill="var(--ink-dark)"/>
    <path d="M367 0 C430 40 470 70 520 0 Z" fill="var(--teal-glass)"/>
    <path d="M560 0 L733 0 L733 720 L680 720 C700 500 640 250 560 0 Z" fill="var(--ink-dark-2)"/>

    <!-- Right panel -->
    <g role="img" aria-label="Photo of modern townhouses">
      <rect x="733" y="0" width="367" height="300" fill="url(#townhousePhoto)"/>
    </g>
    <rect x="733" y="300" width="367" height="420" fill="#e6e6e6"/>
    <path d="M733 180 L960 330 L733 470 Z" fill="var(--ink-dark)"/>
    <path d="M1100 200 L1000 330 L1100 420 Z" fill="var(--ink-dark)"/>
    <path d="M733 300 C850 250 1000 230 1100 150 L1100 0 L1040 0 C1000 150 900 220 733 250 Z" fill="var(--teal-glass)"/>
    <path d="M733 520 C880 470 1000 450 1100 470 L1100 720 L733 720 Z" fill="var(--teal)"/>
    <path d="M733 470 C860 420 980 400 1100 420 L1100 470 C1000 450 880 470 733 520 Z" fill="var(--teal-soft)" opacity=".7"/>
  </svg>

  <p class="intro-copy">If you have ever looked at your RRSP statement and wondered if there was something other than the stocks, bonds or mutual funds your banker or financial advisor have told you are your best choices to grow your investments, well there are. They are
    <span class="highlight">SYNDICATED MORTGAGES!</span></p>

  <h1 class="headline">We Will Help You<br>Finally Make Predictable,<br>STABLE RETURN!</h1>

  <address class="contact">
    <div class="contact-title">Contact Info:</div>
    Tarrowby Wealth Management Inc.<br>
    4 Pellam Rd. W.<br>
    Suite K300
    <div class="contact-gap">Hamilton, ON K2R 7T5<br>
    Office: (905) 463-2918<br>
    www.tarrowbywm.com</div>
    <div class="licence">RBQT Lic # 40963</div>
    <div class="latest-investments">To receive information on our latest investments<br>visit www.cloverpathsavings.ca</div>
  </address>

  <div class="brand">
    <span class="brand-mark"></span>
    <span class="brand-name">TARROWBY</span>
  </div>

  <p class="cover-copy">Tired of investing in the stock market or the latest <strong>mutual fund</strong>?
    <span class="cta">Use Your RRSP to Invest in Real Estate</span></p>
</main>
</body>
</html>
```